Rw construct holdings pty ltd

This is a development and construction company. Website can be set up on our domain rwbuildgroup.net if we could change the domain to rwbuildgroup.com.au would be great

Want the page to have eye catching designs, red, black and white are the preffered colours.

Check out www.tolumine.com.au it is my former company with my partner which i am now venturing out on my own, that is the perfect example of the website i want even allot of the information would be the same

Industry/Entity Type

Construction

Coding

Coded - Design and coding required

Number of Pages Required

5+ page

Requirements
Must have
• Company logo eye catching designs

```html
<!DOCTYPE html>
<html lang="en">
<head>
<meta charset="utf-8">
<title>RW Construct — Development &amp; Construction</title>
<link href="https://fonts.googleapis.com/css2?family=Raleway:wght@400;500;600;700&display=swap" rel="stylesheet">
<style>
:root{
  --red:#d8391f;
  --red-deep:#b7301b;
  --ink:#1b1b1b;
  --dark:#1d1e20;
  --darker:#121314;
  --grey:#f1f3f3;
  --text:#333;
  --white:#fff;
}
*{margin:0;padding:0;box-sizing:border-box}
html,body{width:1200px;height:4725px;overflow:hidden}
body{font-family:"Raleway",Arial,sans-serif;color:var(--text);background:var(--white);position:relative}
.abs{position:absolute}
.center{left:0;width:1200px;text-align:center}
.wordmark{font-family:"Raleway",Arial,sans-serif;font-weight:700;color:var(--ink);letter-spacing:1px;display:flex;align-items:center;gap:10px}
.wordmark .mark{width:14px;height:14px;background:var(--red)}
.btn{position:absolute;width:120px;height:50px;border:5px solid;border-color:var(--red) var(--red) var(--ink) var(--ink);border-radius:28px;font-size:12px;font-weight:700;display:flex;align-items:center;justify-content:center;letter-spacing:.5px}
.btn.on-dark{border-color:var(--red) var(--red) var(--white) var(--white);color:var(--white)}
.btn.on-light{color:var(--ink)}

/* header */
.site-header{top:0;left:0;width:1200px;height:68px;background:var(--white)}
.site-header .wordmark{position:absolute;left:130px;top:22px;font-size:20px}
.nav{position:absolute;right:130px;top:26px;display:flex;gap:22px;font-size:11px;font-weight:500;color:var(--ink);align-items:center}
.nav span{display:flex;align-items:center;gap:5px}
.nav i{display:inline-block;width:9px;height:11px;border:1.5px solid var(--red);border-radius:2px}
.nav .search{width:14px;height:14px;border:1.5px solid #555;border-radius:50%;margin-left:8px}

/* hero */
.hero{top:68px;left:0;width:1200px;height:465px;background:linear-gradient(180deg,#4a5056 0%,#3b3f44 45%,#2c2f33 75%,#4b5050 100%)}
.hero .kicker{top:138px;font-size:22px;color:var(--white);font-weight:500}
.hero h1{top:160px;font-size:58px;color:var(--white);font-weight:700;letter-spacing:1px}
.hero .lede{top:236px;font-size:15px;color:var(--white)}

/* welcome */
.welcome .eyebrow{top:594px;font-size:19px;color:var(--ink);font-weight:500}
.welcome h2{top:625px;font-size:31px;color:var(--ink);font-weight:700}
.welcome h3{top:682px;font-size:14px;color:var(--ink);font-weight:700}
.welcome p{top:732px;left:190px;width:820px;font-size:12.5px;line-height:20px;text-align:center;color:var(--text)}
.feature-image{top:928px;left:130px;width:940px;height:442px;background:var(--white);padding:8px;box-shadow:0 0 0 1px #ddd;z-index:2}
.feature-image div{width:100%;height:100%;background:linear-gradient(180deg,#9bb6d4 0%,#c5d3de 35%,#5a4a42 55%,#2a2626 80%,#7f8a6c 100%)}

/* services */
.services{top:1303px;left:0;width:1200px;height:594px;background:radial-gradient(ellipse at 50% 40%,#2c2d30 0%,var(--darker) 80%)}
.services h2{top:1415px;font-size:32px;color:var(--white);font-weight:600}
.services .intro{top:1473px;left:220px;width:760px;font-size:13px;line-height:20px;color:#ddd;text-align:center}
.service{position:absolute;width:290px;text-align:center;color:var(--white)}
.service svg{display:block;margin:0 auto 8px}
.service h4{font-size:15px;font-weight:600;letter-spacing:.3px;margin-bottom:10px}
.service p{font-size:11.5px;line-height:17px;color:#ddd}

/* about */
.about-graphic{top:2020px;left:130px;width:460px;height:270px;background:linear-gradient(135deg,#2a2a2a 0%,#6b4a3a 45%,#c8c8c8 70%,#3c3c3c 100%);border-radius:130px 70px 90px 130px}
.about h2{position:absolute;left:612px;top:1962px;font-size:32px;color:var(--ink);font-weight:600;line-height:42px}
.about h2 em{font-style:normal;color:var(--red);display:block;padding-left:50px}
.about p{position:absolute;left:610px;top:2064px;width:460px;font-size:12.5px;line-height:20px;color:var(--text)}

/* projects */
.projects{top:2395px;left:0;width:1200px;height:810px;background:var(--dark)}
.projects h2{top:2460px;font-size:32px;color:var(--white);font-weight:600}
.projects .intro{top:2508px;left:220px;width:760px;font-size:13px;line-height:20px;color:#ddd;text-align:center}
.tile{position:absolute;width:300px;height:229px}
.tile.hover{background:var(--red);color:var(--white);text-align:center;padding:58px 30px 0}
.tile.hover h4{font-size:14px;font-weight:600;margin-bottom:14px}
.tile.hover p{font-size:11.5px;line-height:17px}

/* testimonials */
.testimonials h2{top:3268px;font-size:32px;color:var(--ink);font-weight:600}
.testimonials h2 span{color:var(--red)}
.quote{position:absolute;width:460px;height:236px;background:var(--grey);padding:30px 24px}
.quote p{font-size:12px;line-height:20px;color:var(--text)}
.quote b{display:block;margin-top:22px;font-size:13px;color:var(--ink)}
.quote small{font-size:10px;color:#666}

/* contact */
.contact{top:3905px;left:0;width:1200px;height:483px;background:linear-gradient(180deg,var(--red-deep) 0%,#c4391f 60%,#a9301c 100%)}
.contact h2{top:3952px;font-size:32px;color:var(--white);font-weight:500}
.field{position:absolute;border-bottom:1px solid rgba(255,255,255,.6);color:var(--white);font-size:12px;height:42px}
.send{position:absolute;left:552px;top:4296px;width:96px;height:36px;border:2px solid var(--white);border-radius:18px;color:var(--white);font-size:12px;font-weight:700;display:flex;align-items:center;justify-content:center}

/* footer */
.site-footer{top:4388px;left:0;width:1200px;height:337px;background:#0d0d0e}
.site-footer .wordmark{position:absolute;left:0;width:1200px;justify-content:center;top:4470px;font-size:30px;color:var(--white)}
.footnav{top:4552px;font-size:10px;color:var(--white)}
.contacts{position:absolute;top:4590px;left:0;width:1200px;display:flex;justify-content:center;gap:48px;color:var(--white);font-size:13px}
.contacts span{display:flex;align-items:center;gap:10px}
.contacts i{width:40px;height:40px;border:2px solid var(--white);border-left-color:var(--red);border-radius:50%;display:inline-block}
.footer-rule{top:4638px;left:300px;width:600px;height:1px;background:#333}
.copyright{top:4652px;font-size:9px;color:#ccc}
.copyright span{color:var(--red)}
</style>
</head>
<body>

<header class="abs site-header">
  <div class="wordmark"><span class="mark"></span>RW CONSTRUCT</div>
  <nav class="nav">
    <span><i></i>ABOUT US</span>
    <span><i></i>SERVICES</span>
    <span><i></i>PROJECTS</span>
    <span><i></i>CONTACT US</span>
    <span class="search"></span>
  </nav>
</header>

<section class="abs hero" role="img" aria-label="Rendering of modern two-storey townhouses at dusk"></section>
<div class="abs center kicker" style="top:206px;font-size:22px;color:#fff;font-weight:500">CONSTRUCTION</div>
<h1 class="abs center" style="top:228px;font-size:58px;color:#fff;font-weight:700;letter-spacing:1px">RW CONSTRUCT</h1>
<div class="abs center" style="top:304px;font-size:15px;color:#fff">But I must explain to you how all this mistaken idea of denouncing pleasure and praising</div>
<div class="btn on-dark" style="left:540px;top:343px">READ MORE</div>

<section class="welcome">
  <div class="abs center eyebrow">WELCOME TO</div>
  <h2 class="abs center">RW CONSTRUCT</h2>
  <h3 class="abs center">IF YOU USE THIS SITE REGULARLY AND WOULD LIKE TO HELP KEEP THE SITE ON THE INTERNET</h3>
  <p class="abs">But I must explain to you how all this mistaken idea of denouncing pleasure and praising pain was born and I will give you a complete account of the system, and expound the actual teachings of the great explorer of the truth, the master-builder of human happiness. No one rejects, dislikes, or avoids pleasure itself, because it is pleasure, but because those who do not know how to pursue pleasure rationally encounter consequences that are extremely painful.</p>
  <div class="btn on-light" style="left:540px;top:850px">READ MORE</div>
</section>
<div class="abs feature-image"><div role="img" aria-label="Rendering of modern townhouses with timber battens and curved white balconies"></div></div>

<section class="abs services"></section>
<h2 class="abs center services-title" style="top:1415px;font-size:32px;color:#fff;font-weight:600">WHAT WE DO</h2>
<p class="abs" style="top:1473px;left:220px;width:760px;font-size:13px;line-height:20px;color:#ddd;text-align:center">Sed ut perspiciatis unde omnis iste natus error sit voluptatem accusantium doloremque laudantium, totam rem aperiam, eaque ipsa quae ab illo inventore</p>

<div class="service" style="left:135px;top:1540px">
  <svg width="34" height="36" viewBox="0 0 34 36" fill="none" stroke="#d8391f" stroke-width="2"><circle cx="17" cy="11" r="7"/><path d="M5 34c0-8 5-13 12-13s12 5 12 13z"/></svg>
  <h4>FINIBUS BONORUM</h4>
  <p>But I must explain to you how all this mistaken idea of denouncing pleasure and praising pain was born...</p>
</div>
<div class="service" style="left:455px;top:1540px">
  <svg width="44" height="36" viewBox="0 0 44 36" fill="none" stroke="#d8391f" stroke-width="2"><circle cx="24" cy="10" r="7"/><path d="M2 26c8-6 14-6 20-3h10c4 0 4 5 0 5H20M2 34h30l10-8"/></svg>
  <h4>FINIBUS BONORUM</h4>
  <p>But I must explain to you how all this mistaken idea of denouncing pleasure and praising pain was born...</p>
</div>
<div class="service" style="left:775px;top:1540px">
  <svg width="40" height="36" viewBox="0 0 40 36" fill="none" stroke="#d8391f" stroke-width="2"><rect x="4" y="4" width="32" height="12"/><path d="M8 16v18M32 16v18M4 24h32"/></svg>
  <h4>FINIBUS BONORUM</h4>
  <p>But I must explain to you how all this mistaken idea of denouncing pleasure and praising pain was born...</p>
</div>
<div class="service" style="left:135px;top:1692px">
  <svg width="34" height="36" viewBox="0 0 34 36" fill="none" stroke="#d8391f" stroke-width="2"><circle cx="17" cy="17" r="14"/><path d="M10 13h14M10 19h10"/></svg>
  <h4>FINIBUS BONORUM</h4>
  <p>But I must explain to you how all this mistaken idea of denouncing pleasure and praising pain was born...</p>
</div>
<div class="service" style="left:455px;top:1692px">
  <svg width="30" height="36" viewBox="0 0 30 36" fill="none" stroke="#d8391f" stroke-width="2"><path d="M15 3a10 10 0 0 0-6 18v5h12v-5A10 10 0 0 0 15 3zM10 31h10"/></svg>
  <h4>FINIBUS BONORUM</h4>
  <p>But I must explain to you how all this mistaken idea of denouncing pleasure and praising pain was born...</p>
</div>
<div class="service" style="left:775px;top:1692px">
  <svg width="36" height="36" viewBox="0 0 36 36" fill="none" stroke="#d8391f" stroke-width="2"><circle cx="18" cy="18" r="6"/><circle cx="18" cy="18" r="13" stroke-dasharray="5 4"/></svg>
  <h4>FINIBUS BONORUM</h4>
  <p>But I must explain to you how all this mistaken idea of denouncing pleasure and praising pain was born...</p>
</div>

<section class="about">
  <div class="abs about-graphic" role="img" aria-label="Large decorative shape filled with a townhouse rendering"></div>
  <h2>EXCEPTEUR SINT OCCAECAT<em>CUPIDATAT PROIDENT</em></h2>
  <p>But I must explain to you how all this mistaken idea of denouncing pleasure and praising pain was born and I will give you a complete account of the system, and expound the actual teachings of the great explorer of the truth, the master-builder of human happiness. No one rejects, dislikes, or avoids pleasure itself, because it is pleasure, but because those who do not know how to pursue pleasure rationally encounter consequences that are extremely painful. Nor again is there anyone who loves or pursues or desires to obtain pain of itself, because it is pain, but because occasionally circumstances occur in which toil and pain can procure him some great pleasure.</p>
  <div class="btn on-light" style="left:780px;top:2272px">READ MORE</div>
</section>

<section class="abs projects"></section>
<h2 class="abs center" style="top:2460px;font-size:32px;color:#fff;font-weight:600">OUR PROJECTS</h2>
<p class="abs" style="top:2508px;left:220px;width:760px;font-size:13px;line-height:20px;color:#ddd;text-align:center">Sed ut perspiciatis unde omnis iste natus error sit voluptatem accusantium doloremque laudantium, totam rem aperiam, eaque ipsa quae ab illo inventore</p>
<div class="tile" style="left:130px;top:2574px;background:linear-gradient(160deg,#f2f2f2,#cfc7bd 60%,#8a6a50)" role="img" aria-label="Open-plan kitchen with white island and timber floor"></div>
<div class="tile hover" style="left:450px;top:2574px">
  <h4>ARCHITECTO BEATAE</h4>
  <p>But I must explain to you how all mistaken idea of denouncing pleasure and praising</p>
  <svg width="14" height="10" viewBox="0 0 14 10" style="margin-top:14px" fill="none" stroke="#fff" stroke-width="1.6"><path d="M1 5h11M8 1l4 4-4 4"/></svg>
</div>
<div class="tile" style="left:770px;top:2574px;background:linear-gradient(160deg,#f4f4f4,#dcdcdc 55%,#bda88e)" role="img" aria-label="Bright living room with grey sofa"></div>
<div class="tile" style="left:130px;top:2820px;background:linear-gradient(180deg,#2d4f98 0%,#5a7ab8 45%,#6a6a6a 70%,#5a6a4a)" role="img" aria-label="Modern two-storey house at dusk"></div>
<div class="tile" style="left:450px;top:2820px;background:linear-gradient(160deg,#f0f0f0,#d4cfc8 55%,#6b5a4d)" role="img" aria-label="Living area with staircase and leather armchairs"></div>
<div class="tile" style="left:770px;top:2820px;background:linear-gradient(150deg,#f4f4f4,#d8d8d8 50%,#2a2a2a 85%)" role="img" aria-label="Floating timber staircase with glass balustrade"></div>
<div class="btn on-dark" style="left:540px;top:3085px">READ MORE</div>

<section class="testimonials">
  <h2 class="abs center">CUSTOMER <span>SAY’S</span></h2>
  <div class="quote" style="left:130px;top:3337px"><p>“But I must explain to you how all this mistaken idea of denouncing pleasure and praising pain was born and I will give you a complete account of the system, and expound the actual teachings of the great explorer of the truth, the master-builder of human happiness ed quia non numquam eius modi tempora incidunt ut labore et dolore magnam aliquam quaerat voluptatem.”</p><b>Mara Elwood</b><small>Westbrook</small></div>
  <div class="quote" style="left:610px;top:3337px"><p>“But I must explain to you how all this mistaken idea of denouncing pleasure and praising pain was born and I will give you a complete account of the system, and expound the actual teachings of the great explorer of the truth, the master-builder of human happiness ed quia non numquam eius modi tempora incidunt ut labore et dolore magnam aliquam quaerat voluptatem.”</p><b>Mara Elwood</b><small>Westbrook</small></div>
  <div class="quote" style="left:130px;top:3595px"><p>“But I must explain to you how all this mistaken idea of denouncing pleasure and praising pain was born and I will give you a complete account of the system, and expound the actual teachings of the great explorer of the truth, the master-builder of human happiness ed quia non numquam eius modi tempora incidunt ut labore et dolore magnam aliquam quaerat voluptatem.”</p><b>Mara Elwood</b><small>Westbrook</small></div>
  <div class="quote" style="left:610px;top:3595px"><p>“But I must explain to you how all this mistaken idea of denouncing pleasure and praising pain was born and I will give you a complete account of the system, and expound the actual teachings of the great explorer of the truth, the master-builder of human happiness ed quia non numquam eius modi tempora incidunt ut labore et dolore magnam aliquam quaerat voluptatem.”</p><b>Mara Elwood</b><small>Westbrook</small></div>
</section>

<section class="abs contact" role="img" aria-label="Red-tinted townhouse rendering behind the contact form"></section>
<h2 class="abs center" style="top:3952px;font-size:32px;color:#fff;font-weight:500">SAY HELLO</h2>
<div class="field" style="left:243px;top:4026px;width:348px">First Name:</div>
<div class="field" style="left:608px;top:4026px;width:348px">First Name:</div>
<div class="field" style="left:243px;top:4094px;width:348px">Email:</div>
<div class="field" style="left:608px;top:4094px;width:348px">Phone:</div>
<div class="field" style="left:243px;top:4162px;width:713px;height:110px">Message:</div>
<div class="send">SEND</div>

<footer class="abs site-footer"></footer>
<div class="wordmark" style="position:absolute;left:0;width:1200px;justify-content:center;top:4468px;font-size:32px;color:#fff"><span class="mark"></span>RW CONSTRUCT</div>
<div class="abs center footnav" style="top:4553px;font-size:10px;color:#fff">ABOUT US &nbsp;|&nbsp; SERVICES &nbsp;|&nbsp; PROJECTS &nbsp;|&nbsp; CONTACT US</div>
<div class="contacts">
  <span><i></i>+2 456 711 38</span>
  <span><i></i>admin@rwbuildgroup.net</span>
  <span><i></i>Follow us</span>
</div>
<div class="abs footer-rule"></div>
<div class="abs center copyright" style="top:4652px;font-size:9px;color:#ccc">COPYRIGHT © 2021 <span style="color:#d8391f">RW CONSTRUCT</span>. ALL RIGHTS RESERVED.</div>

</body>
</html>
```